Law Firm Business Card

This is a business card for a law firm that serves US military and veterans.

The card must have ONLY the following (we want an uncluttered look):

- Company logo (PNG, GIF, JPEG copies uploaded)
- A tagline reading: "a law firm for service members and veterans"
- My name and title: "Martin Okello" and "Attorney"
- My email: "martin.okello@harborlinecounsel.com"
- My number: "855-FILE-NOW (345-3669)"

We are looking for a clean, simple layout with only the above information, likely printed on a bright white cotton stock. The font of our logo is DIN 1451, and the font used on our website is Helvetica Neue. The color of our logo is #336699, and we probably want the tagline in that color also, and my contact information in a dark grey. Please review our website at www.harborlinecounsel.com to ensure your card design complements our website style.

Thanks and we look forward to seeing your submissions.

A few notes:

- Two-sided submissions are ok
- Please don't add graphics (scales of justice, judges hammer, etc)

```html
<!DOCTYPE html>
<html lang="en">
<head>
<meta charset="utf-8">
<title>Harborline Counsel – Business Card</title>
<link rel="stylesheet" href="https://fonts.googleapis.com/css2?family=Arimo:wght@400;700&display=swap">
<style>
  :root {
    --brand-blue: #336699;
    --paper-white: #ffffff;
    --text-on-blue: #ffffff;
    --page-bg: #ffffff;
  }
  * { box-sizing: border-box; margin: 0; padding: 0; }
  html, body {
    width: 1200px;
    height: 721px;
    overflow: hidden;
    background: var(--page-bg);
  }
  .card {
    display: flex;
    width: 1200px;
    height: 721px;
    font-family: "Arimo", "Helvetica Neue", Helvetica, Arial, sans-serif;
  }
  .brand-panel {
    position: relative;
    width: 440px;
    height: 100%;
    background: var(--paper-white);
    display: flex;
    align-items: center;
    justify-content: center;
  }
  .brand-stack {
    writing-mode: vertical-rl;
    transform: rotate(180deg);
    display: flex;
    flex-direction: column;
    align-items: flex-start;
    color: var(--brand-blue);
  }
  .brand-name {
    font-weight: 700;
    font-size: 88px;
    line-height: 1;
    letter-spacing: 1px;
    text-transform: uppercase;
  }
  .brand-name-sub {
    font-weight: 700;
    font-size: 48px;
    line-height: 1.05;
    letter-spacing: 14px;
    text-transform: uppercase;
    margin-left: 4px;
    margin-top: 2px;
  }
  .tagline {
    font-weight: 400;
    font-size: 27px;
    line-height: 1;
    margin-top: 46px;
  }
  .contact-panel {
    flex: 1;
    height: 100%;
    background: var(--brand-blue);
    color: var(--text-on-blue);
    padding: 200px 70px 0 78px;
    display: flex;
    flex-direction: column;
  }
  .person-name {
    font-size: 48px;
    font-weight: 400;
    line-height: 1.1;
  }
  .person-title {
    font-size: 28px;
    font-weight: 400;
    margin-top: 12px;
  }
  .contact-list {
    list-style: none;
    margin-top: 158px;
  }
  .contact-list li {
    font-size: 29px;
    line-height: 1.45;
  }
</style>
</head>
<body>
  <main class="card">
    <section class="brand-panel">
      <div class="brand-stack">
        <span class="brand-name">Harborline</span>
        <span class="brand-name-sub">Counsel</span>
        <p class="tagline">A law firm for service members and veterans</p>
      </div>
    </section>
    <section class="contact-panel">
      <h1 class="person-name">Martin Okello</h1>
      <p class="person-title">Attorney</p>
      <ul class="contact-list">
        <li class="contact-phone">855-FILE-NOW (345-3669)</li>
        <li class="contact-email">martin.okello@harborlinecounsel.com</li>
      </ul>
    </section>
  </main>
</body>
</html>
```